TLPB Business Card Design

Business card for sole operator professional civil and traffic engineer.
Clients are developers and planners who require assistance with traffic strategic master planning advice and design development for access and infrastructure associated with the development.
Colours already in use are greens for the business name and black for other legend. The attached file shows the letterhead template which is currently in use.
Target Market(s)
Professional Clients in development industry
Most clients known to the Principal and card is mostly required to allow ongoing contact
Industry/Entity Type
Business
Contact Information for Business Card
DESMOND HALVERTON CONSULTING SERVICES
ABN 37 818 502 194
PO Box 871 KERRAWAY NSW 2619
Desmond Halverton 0431 558 906
desmond.halverton@quillmarsh.net

```html
<!DOCTYPE html>
<html lang="en">
<head>
<meta charset="utf-8">
<title>TLPB Business Card</title>
<link rel="stylesheet" href="https://fonts.googleapis.com/css2?family=Arimo:wght@400;700&family=Open+Sans:wght@400;600&display=swap">
<style>
  :root {
    --page-bg: #e9e7e2;
    --card-white: #ffffff;
    --brand-green: #1fbf62;
    --brand-green-dark: #14a24e;
    --leaf-green: #5fb236;
    --leaf-green-light: #9ccc55;
    --lime-rule: #b6d94a;
    --ink: #111111;
    --ink-soft: #2b2b2b;
    --title-green: #27c46a;
  }
  * { box-sizing: border-box; margin: 0; padding: 0; }
  html, body {
    width: 1200px; height: 900px; overflow: hidden;
    background: var(--page-bg);
  }
  .stage {
    width: 1200px; height: 900px;
    display: flex; align-items: center; justify-content: center;
  }
  .business-card {
    position: relative;
    width: 490px; height: 800px;
    background: var(--card-white);
    box-shadow: 0 10px 30px rgba(0,0,0,0.18);
    overflow: hidden;
    font-family: "Arimo", Arial, sans-serif;
    display: flex; flex-direction: column;
  }
  .brand-band {
    flex: 0 0 auto;
    height: 140px;
    background: linear-gradient(180deg, var(--brand-green) 0%, var(--brand-green-dark) 100%);
    display: flex; flex-direction: column; align-items: center; justify-content: center;
    color: #fff;
    text-align: center;
    position: relative;
  }
  .brand-rule {
    flex: 0 0 auto;
    height: 5px;
    margin-top: 8px;
    background: var(--lime-rule);
  }
  .brand-name {
    font-weight: 700; font-size: 29px; letter-spacing: 0.5px; line-height: 1.15;
    text-shadow: 0 0 6px rgba(255,255,255,0.55);
  }
  .brand-sub { font-size: 25px; }
  .contact-block {
    flex: 1 1 auto;
    padding: 40px 24px 0;
    text-align: center;
    color: var(--ink-soft);
  }
  .person-name { font-weight: 700; font-size: 40px; line-height: 1.15; color: var(--ink); }
  .person-title { font-weight: 700; font-size: 22px; line-height: 1.2; color: var(--title-green); margin-top: 2px; }
  .postal { font-size: 20px; line-height: 1.35; margin-top: 18px; }
  .details { font-size: 20px; line-height: 1.35; margin-top: 16px; }
  .details .email { color: var(--ink); }
  .service-band {
    flex: 0 0 320px;
    position: relative;
    background: linear-gradient(180deg, var(--leaf-green) 0%, var(--leaf-green-light) 55%, var(--leaf-green) 100%);
    border-top: 5px solid var(--lime-rule);
  }
  .service-band::before {
    content: ""; position: absolute; left: 0; right: 0; top: 6px;
    height: 3px; background: var(--card-white);
  }
  .service-band::after {
    content: ""; position: absolute; left: 0; right: 0; bottom: 38px;
    height: 3px; background: var(--card-white);
  }
  .service-summary {
    padding: 40px 26px 0;
    font-family: "Open Sans", Arial, sans-serif;
    font-size: 20px; line-height: 1.45;
    color: rgba(255,255,255,0.92);
    text-align: center;
  }
</style>
</head>
<body>
<main class="stage">
  <article class="business-card">
    <header class="brand-band">
      <div class="brand-name">DESMOND HALVERTON</div>
      <div class="brand-name brand-sub">CONSULTING SERVICES</div>
    </header>
    <div class="brand-rule"></div>
    <section class="contact-block">
      <h1 class="person-name">Your Name Here</h1>
      <p class="person-title">Title Here</p>
      <p class="postal">PO Box 871 KERRAWAY NSW 2619<br>Desmond Halverton</p>
      <p class="details">ABN : 37 818 502 194<br>Phone : 0431 558 906<br><span class="email">desmond.halverton@quillmarsh.net</span></p>
    </section>
    <footer class="service-band">
      <p class="service-summary">Clients are developers and planners who require assistance with traffic strategic master planning advice and design development for access and infrastructure associated with the development.</p>
    </footer>
  </article>
</main>
</body>
</html>
```